Spanish winery needs a label design for a red, white and rosé wine.

We need a front and back label for our representee Vidal Arandes SL, a wine producer in the Spanish region of Extremadura.

Trademark: Sereniza. Sereniza means balanced in English. The message is that the wine show the equilibrium of the blends specially produced for this project, it is balanced in the mounth and nose and it,s a good balance between quality and price.

Target: Wine targets entry level market retail sector in Europe so it cannot be too fancy.

Style: Spanish wines are better seen with a classic touch in the design although a bit of modernity is required.

Number of labels: 3 front and 3 back labels required although you can use the same design and just change the colors. Bottle is a bordeaux style 30 mm high with an screw cup closure, green for the red and transparent for the white and rosé.

Labels size: front max 90 (wide)x130 (high)mm. Back max 85 (w)x85(h)mm.

Information to include in the front label: Trademark, type of wine (red, white or rosé), two short lines of text with tasting notes (see texts on doc file), capacity 75cl, ABV:11º vol. Bottled by Vidal Arandes SL C/Tarifa 27. 06480 Villar del Conde (Badajoz). Spain.

Information to be included in the back label:trademark, type of wine, tasting notes (see texts on doc file), Capacity 75cl, Filling control mark: E, Barcode, Allergy advise, Contains sulfites advise, Pregnant women advise.

Paper: Shiny or matt paper with possibility of foil printing. No embossed effects.

Please see attached Vega Lunar label as a reference of the necessary information to be contained by labels.
Updates

Reason: We would like to give a bit more of time to those that have accepted and have not yet submitted a design.

Target Market(s)

Entry level european consumers

Industry/Entity Type

Retail

Requirements
Nice to have
• Maybe a clasical scale, old coins (balanced in cost).... Balance is the route to follow.

```html
<!DOCTYPE html>
<html lang="en">
<head>
<meta charset="utf-8">
<title>Sereniza – Front Labels</title>
<link href="https://fonts.googleapis.com/css2?family=Cinzel:wght@400;600&family=Cormorant+Garamond:ital,wght@0,500;0,600;1,500&display=swap" rel="stylesheet">
<style>
  :root {
    --canvas-bg: #f4f1ec;
    --gold: #d9b25a;
    --gold-light: #f3dc95;
    --gold-dark: #8a6420;
    --cream: #f8ecd0;
    --ink: #3a2410;
    --text-light: #fbf3df;

    --white-top: #3b2f1c;
    --white-mid: #6e5a35;
    --white-low: #a08a5e;

    --red-top: #4a1410;
    --red-mid: #8c2a1e;
    --red-low: #b24a30;

    --rose-top: #5a1d1a;
    --rose-mid: #9a3a2c;
    --rose-low: #c0705a;
  }
  * { box-sizing: border-box; margin: 0; padding: 0; }
  html, body { width: 1200px; height: 1000px; overflow: hidden; }
  body {
    background: var(--canvas-bg);
    font-family: "Cormorant Garamond", Georgia, serif;
    display: flex;
    align-items: center;
    justify-content: center;
    gap: 45px;
  }

  .label {
    position: relative;
    width: 340px;
    height: 480px;
    padding: 6px;
    background: linear-gradient(135deg, var(--gold-light), var(--gold) 40%, var(--gold-dark) 100%);
    box-shadow: 0 6px 18px rgba(0,0,0,.18);
  }
  .label__inner {
    position: relative;
    width: 100%;
    height: 100%;
    border: 1px solid var(--gold-light);
    overflow: hidden;
    display: flex;
    flex-direction: column;
    align-items: center;
  }
  .label__artwork {
    position: absolute;
    inset: 0;
    z-index: 0;
  }
  .label--white .label__artwork {
    background:
      radial-gradient(ellipse at 55% 78%, rgba(232,196,110,.75), transparent 45%),
      linear-gradient(180deg, var(--white-top) 0%, var(--white-mid) 45%, var(--white-low) 100%);
  }
  .label--red .label__artwork {
    background:
      radial-gradient(ellipse at 55% 78%, rgba(232,190,100,.7), transparent 45%),
      linear-gradient(180deg, var(--red-top) 0%, var(--red-mid) 45%, var(--red-low) 100%);
  }
  .label--rose .label__artwork {
    background:
      radial-gradient(ellipse at 55% 78%, rgba(236,196,120,.7), transparent 45%),
      linear-gradient(180deg, var(--rose-top) 0%, var(--rose-mid) 45%, var(--rose-low) 100%);
  }

  .label__brand {
    position: relative;
    z-index: 1;
    margin-top: 52px;
    display: flex;
    align-items: center;
    gap: 8px;
    font-family: "Cinzel", "Times New Roman", serif;
    font-weight: 600;
    font-size: 30px;
    letter-spacing: 1px;
    color: var(--gold-light);
  }
  .label__brand-dot {
    width: 8px; height: 8px; border-radius: 50%;
    background: var(--gold-light);
  }

  .label__type {
    position: relative;
    z-index: 1;
    margin-top: 34px;
    width: 100%;
    padding: 3px 0;
    background: linear-gradient(90deg, var(--gold-dark), var(--gold-light) 50%, var(--gold-dark));
  }
  .label__type-text {
    display: block;
    background: var(--cream);
    text-align: center;
    font-family: "Cinzel", "Times New Roman", serif;
    font-size: 17px;
    letter-spacing: 1.5px;
    color: var(--ink);
    padding: 4px 0 3px;
  }

  .label__notes {
    position: relative;
    z-index: 1;
    margin-top: 10px;
    padding: 0 26px;
    text-align: center;
    font-size: 14px;
    line-height: 1.25;
    color: var(--text-light);
  }

  .label__footer {
    position: relative;
    z-index: 1;
    margin-top: auto;
    margin-bottom: 12px;
    width: 100%;
    padding: 0 16px;
    text-align: center;
    color: var(--text-light);
    font-size: 10px;
    line-height: 1.3;
  }
  .label__specs {
    display: flex;
    justify-content: space-between;
    margin-top: 6px;
    font-size: 10.5px;
  }
</style>
</head>
<body>

  <section class="label label--white">
    <div class="label__inner">
      <div class="label__artwork" role="img" aria-label="Photograph of stacked old gold coins on a dark warm background with a gold ornament crest at the top"></div>
      <div class="label__brand"><span class="label__brand-dot"></span>Sereniza</div>
      <div class="label__type"><span class="label__type-text">White Wine</span></div>
      <p class="label__notes">A refreshing Spanish white wine<br>with crisp citrus and orchard fruit flavours</p>
      <div class="label__footer">
        <p>Bottled by Vidal Arandes SL<br>C/Tarifa 27. 06480 Villar del Conde (Badajoz). Spain</p>
        <div class="label__specs"><span>75cl</span><span>ABV 11º</span><span>11% vol</span></div>
      </div>
    </div>
  </section>

  <section class="label label--red">
    <div class="label__inner">
      <div class="label__artwork" role="img" aria-label="Photograph of stacked old gold coins on a deep red background with a gold ornament crest at the top"></div>
      <div class="label__brand"><span class="label__brand-dot"></span>Sereniza</div>
      <div class="label__type"><span class="label__type-text">Red Wine</span></div>
      <p class="label__notes">Seductively soft and smooth red wine<br>displaying delicious fruit flavours</p>
      <div class="label__footer">
        <p>Bottled by Vidal Arandes SL<br>C/Tarifa 27. 06480 Villar del Conde (Badajoz). Spain</p>
        <div class="label__specs"><span>75cl</span><span>ABV 11º</span><span>11% vol</span></div>
      </div>
    </div>
  </section>

  <section class="label label--rose">
    <div class="label__inner">
      <div class="label__artwork" role="img" aria-label="Photograph of stacked old gold coins on a rosy red background with a gold ornament crest at the top"></div>
      <div class="label__brand"><span class="label__brand-dot"></span>Sereniza</div>
      <div class="label__type"><span class="label__type-text">Rosé Wine</span></div>
      <p class="label__notes">A refreshing Spanish Rosado Sumoll<br>with ripe strawberry and raspberry flavours</p>
      <div class="label__footer">
        <p>Bottled by Vidal Arandes SL<br>C/Tarifa 27. 06480 Villar del Conde (Badajoz). Spain</p>
        <div class="label__specs"><span>75cl</span><span>ABV 11º</span><span>11% vol</span></div>
      </div>
    </div>
  </section>

</body>
</html>
```